Business Card Re-Design for a Lighting Designer

I would like my business card re-designed. It is currently high gloss and they scratch too easily. I don not think the current design lends itself well to a matte finish. I have included the current design for reference along with our company logo.
Check out our website for current branding.
http://www.brambleorchidstudio.example

Updates
Some of the top contenders are muslim and it is a holiday for them. I do not want to discriminate and would expect the same courtesy for holidays we celebrate.
Target Market(s)
Interior Designers, Architects
Contact Information for Business Card
Logo - Name, Title, Address, Telephone Number and Extension, Email
Font styles to use
Requirements
Must have
- All the information listed on the current business card. If you use Red, it needs to be the red from our logo.
Nice to have
- Vertical and Horizontal Designs will be entertained.
Should not have
- Requirements for a glossy finish...should not look too corporate since we are a design firm.

```html
<!DOCTYPE html>
<html lang="en">
<head>
<meta charset="utf-8">
<title>Bramble Orchid Studio — Business Card</title>
<link href="https://fonts.googleapis.com/css2?family=Roboto+Condensed:wght@300;400;700&display=swap" rel="stylesheet">
<style>
  :root {
    --brand-red: #9a1b1f;
    --ink: #1d1d1d;
    --paper: #ffffff;
    --backdrop: #3d3d3d;
  }
  * { box-sizing: border-box; margin: 0; padding: 0; }
  html, body {
    width: 1200px; height: 1200px; overflow: hidden;
    background: var(--backdrop);
    font-family: "Roboto Condensed", "Arial Narrow", sans-serif;
  }
  .sheet {
    width: 1200px; height: 1200px;
    display: flex; align-items: center; justify-content: center; gap: 16px;
  }
  .card {
    width: 560px; height: 342px; position: relative;
    box-shadow: 0 4px 14px rgba(0,0,0,.35);
  }
  .card--front { background: var(--paper); }
  .card--back {
    background: var(--brand-red);
    display: flex; flex-direction: column; align-items: center; justify-content: center;
  }
  .brand { position: absolute; left: 46px; top: 49px; width: 190px; }
  .brand__square { width: 120px; height: 120px; background: var(--brand-red); }
  .brand__name {
    margin-top: 14px; color: var(--ink); font-weight: 300;
    font-size: 31px; line-height: 1.05; letter-spacing: -0.3px; text-transform: uppercase;
  }
  .contact { position: absolute; left: 256px; top: 128px; }
  .contact__name { color: var(--brand-red); font-weight: 700; font-size: 22px; letter-spacing: .2px; }
  .contact__title { color: var(--ink); font-weight: 700; font-size: 16px; letter-spacing: 1.2px; margin-bottom: 12px; }
  .contact__list { list-style: none; }
  .contact__item {
    display: flex; align-items: flex-start; gap: 8px;
    color: var(--ink); font-size: 15.5px; line-height: 20px;
  }
  .contact__icon { width: 13px; height: 13px; margin-top: 3px; flex: none; }
  .contact__icon--blank { visibility: hidden; }
  .back-brand { display: flex; flex-direction: column; align-items: center; }
  .back-brand__square { width: 84px; height: 84px; background: var(--paper); }
  .back-brand__name {
    margin-top: 10px; color: var(--paper); font-weight: 300;
    font-size: 19px; text-transform: uppercase; letter-spacing: .3px;
  }
  .back-url {
    margin-top: 26px; color: var(--paper); font-size: 15px; letter-spacing: 2.6px;
  }
</style>
</head>
<body>
<main class="sheet">
  <section class="card card--front" aria-label="Card front">
    <div class="brand">
      <div class="brand__square"></div>
      <p class="brand__name">Bramble Orchid<br>Studio</p>
    </div>
    <div class="contact">
      <h1 class="contact__name">MAREN OAKLEY</h1>
      <p class="contact__title">PRINCIPAL</p>
      <ul class="contact__list">
        <li class="contact__item">
          <svg class="contact__icon" viewBox="0 0 14 14"><circle cx="7" cy="7" r="7" fill="#9a1b1f"/><path d="M7 3.2a2.6 2.6 0 0 0-2.6 2.6C4.4 7.8 7 10.8 7 10.8s2.6-3 2.6-5A2.6 2.6 0 0 0 7 3.2z" fill="#fff"/><circle cx="7" cy="5.8" r="1" fill="#9a1b1f"/></svg>
          <span>210 Fernhill Row, Suite 130</span>
        </li>
        <li class="contact__item">
          <svg class="contact__icon contact__icon--blank" viewBox="0 0 14 14"></svg>
          <span>Riverton, Georgia 30999 USA</span>
        </li>
        <li class="contact__item">
          <svg class="contact__icon" viewBox="0 0 14 14"><circle cx="7" cy="7" r="7" fill="#9a1b1f"/><rect x="3.6" y="4.6" width="6.8" height="4.8" fill="#fff"/><path d="M3.6 4.6 7 7.4l3.4-2.8" fill="none" stroke="#9a1b1f" stroke-width=".8"/></svg>
          <span>maren@brambleorchidstudio.example</span>
        </li>
        <li class="contact__item">
          <svg class="contact__icon" viewBox="0 0 14 14"><circle cx="7" cy="7" r="7" fill="#9a1b1f"/><path d="M4.6 3.6l1.3-.2.8 1.8-.9.7c.4.9 1.1 1.6 2 2l.7-.9 1.8.8-.2 1.3c-3 .3-5.8-2.5-5.5-5.5z" fill="#fff"/></svg>
          <span>555 014 2290 x 1</span>
        </li>
        <li class="contact__item">
          <svg class="contact__icon" viewBox="0 0 14 14"><circle cx="7" cy="7" r="7" fill="#9a1b1f"/><circle cx="7" cy="7" r="3.6" fill="none" stroke="#fff" stroke-width=".9"/><path d="M3.4 7h7.2M7 3.4c-1.6 2-1.6 5.2 0 7.2M7 3.4c1.6 2 1.6 5.2 0 7.2" fill="none" stroke="#fff" stroke-width=".7"/></svg>
          <span>www.brambleorchidstudio.example</span>
        </li>
      </ul>
    </div>
  </section>

  <section class="card card--back" aria-label="Card back">
    <div class="back-brand">
      <div class="back-brand__square"></div>
      <p class="back-brand__name">Bramble Orchid Studio</p>
    </div>
    <p class="back-url">www.brambleorchidstudio.example</p>
  </section>
</main>
</body>
</html>
```